Copper Pathfinders (WordPress Hosting)

The site I would like is a robust message board. Each forum will be a group of people discussing and tracking their goals. I would also like areas
on the site for advertisers. Something similar to https://uprising.geargrowthhub.com/

Coding

Coded - Design and coding required

Number of Pages Required

1 page

Requirements
Must have
• Message Board

```html
<!DOCTYPE html>
<html lang="en">
<head>
<meta charset="utf-8">
<title>Ember Ridge Forums</title>
<link href="https://fonts.googleapis.com/css2?family=Lato:wght@400;700;900&display=swap" rel="stylesheet">
<style>
:root{
  --orange:#ee5522;
  --green:#86bc25;
  --dark:#3a3a3a;
  --row:#f4f4f4;
  --line:#e2e2e2;
  --text:#333;
  --muted:#6b6b6b;
  --footer:#e3e3e3;
}
*{box-sizing:border-box;margin:0;padding:0}
html,body{width:1200px;height:2677px;overflow:hidden;background:#fff}
body{font-family:'Lato',sans-serif;color:var(--text)}
.page{width:1155px;height:2576px;transform:scale(1.039);transform-origin:0 0;position:relative}
.hero{height:192px;position:relative;background:linear-gradient(100deg,#3b2a22 0%,#5a4030 30%,#2c2a2a 55%,#6a4a35 80%,#3a2c25 100%)}
.hero-photo{position:absolute;inset:0}
.search{position:absolute;left:72px;top:85px;width:173px;height:36px;border:1px solid #fff;color:#fff;font-size:13px;padding:10px 11px}
.search svg{position:absolute;right:10px;top:11px}
.brand{position:absolute;left:0;right:0;top:92px;text-align:center;font-weight:900;font-size:30px;color:var(--green);letter-spacing:.5px}
.brand .dot{display:inline-block;width:14px;height:14px;border-radius:50%;background:var(--green);margin-right:10px;vertical-align:3px}
.signin{position:absolute;left:849px;top:96px;color:#fff;font-size:13px;font-weight:700}
.signup{position:absolute;left:1011px;top:85px;width:72px;height:36px;border:1px solid #fff;color:#fff;font-size:13px;font-weight:700;text-align:center;line-height:34px}
.nav{height:51px;background:var(--orange);display:flex;justify-content:center}
.nav a{color:#fff;font-size:13.5px;font-weight:700;text-transform:uppercase;line-height:51px;padding:0 20px;text-decoration:none}
.nav a.active{background:var(--green)}
.subnav{height:39px;background:var(--green);padding-left:72px;display:flex;gap:30px;align-items:center;font-size:13px;font-weight:700}
.subnav .current{color:#1e2a0a}
.subnav a{color:#fff;text-decoration:none}
.wrap{margin:0 72px}
.browsing{margin-top:14px;border:1px solid var(--line)}
.browsing-head{height:44px;background:var(--dark);color:#fff;font-size:12px;font-weight:700;padding:0 13px;line-height:44px}
.browsing-head span{color:var(--green);margin-left:6px}
.browsing-body{height:43px;background:var(--row);font-size:13px;padding:0 14px;line-height:43px}
.forums-title{display:flex;justify-content:space-between;align-items:center;margin-top:16px;height:32px}
.forums-title h1{font-size:21px;font-weight:700;padding-left:3px;color:#333}
.btn-new{background:var(--green);color:#fff;font-size:14px;font-weight:700;width:140px;height:32px;line-height:32px;text-align:center}
.section{margin-top:14px}
.section:first-of-type{margin-top:0}
.sec-head{height:44px;background:var(--dark);color:#fff;font-size:12px;font-weight:700;padding:0 14px;display:flex;justify-content:space-between;align-items:center;text-transform:uppercase}
.sec-body{background:var(--row);border:1px solid var(--line);border-top:0;padding:5px 13px 6px}
.row{height:82px;display:flex;align-items:center;border-bottom:1px solid var(--line)}
.row:last-child{border-bottom:0}
.chat{width:38px;height:38px;border-radius:50%;background:#fff;border:1px solid var(--line);display:flex;align-items:center;justify-content:center;margin-left:1px}
.info{margin-left:15px;width:570px}
.info h3{font-size:18px;font-weight:400;color:var(--orange);line-height:22px}
.info p{font-size:14px;line-height:20px;color:#333}
.count{width:110px;text-align:center;margin-left:6px}
.count b{display:block;font-size:26px;font-weight:400;color:var(--orange);line-height:28px}
.count span{font-size:14px;color:#555}
.avatar{width:40px;height:40px;border-radius:50%;background:#fff;border:1px solid var(--line);display:flex;align-items:center;justify-content:center;margin-left:28px}
.last{margin-left:8px;font-size:12px;line-height:17px;color:#333}
.last strong{display:block;color:var(--green);font-size:13px;font-weight:700}
.collapsed{margin-top:11px}
.collapsed:first-of-type{margin-top:44px}
.footer{position:absolute;left:0;right:0;top:2458px;height:118px;background:var(--footer);text-align:center}
.footer p{margin-top:30px;font-size:13px;color:#666}
.social{display:flex;justify-content:center;gap:17px;margin-top:16px}
.social i{width:21px;height:21px;border-radius:50%;background:#777;display:block}
</style>
</head>
<body>
<div class="page">
  <header class="hero">
    <div class="hero-photo" role="img" aria-label="Photo of athletes training in a gym, darkened"></div>
    <div class="search">Search...
      <svg width="12" height="12" viewBox="0 0 12 12"><circle cx="5" cy="5" r="3.8" fill="none" stroke="#86bc25" stroke-width="1.8"/><line x1="8" y1="8" x2="11" y2="11" stroke="#86bc25" stroke-width="1.8"/></svg>
    </div>
    <div class="brand"><span class="dot"></span>EMBER RIDGE</div>
    <div class="signin">Existing user? Sign In &nbsp;<svg width="8" height="6" viewBox="0 0 8 6"><path d="M1 1l3 3 3-3" fill="none" stroke="#fff" stroke-width="1.2"/></svg></div>
    <div class="signup">Sign Up</div>
  </header>
  <nav class="nav">
    <a>Browse</a><a>Ember Ridge</a><a>Private Coaching</a><a class="active">Browse</a><a>5 Week Challenge</a><a>Activity</a><a>Leaderboard</a>
  </nav>
  <div class="subnav"><span class="current">Forums</span><a>Contact / Help</a></div>

  <main class="wrap">
    <div class="browsing">
      <div class="browsing-head">RECENTLY BROWSING <span>1 MEMBER</span></div>
      <div class="browsing-body">Dovrin</div>
    </div>
    <div class="forums-title"><h1>FORUMS</h1><div class="btn-new">Start New Topic</div></div>

    <div style="margin-top:14px">
    <section class="section">
      <div class="sec-head">Welcome<svg width="12" height="8" viewBox="0 0 12 8"><path d="M1.5 1.5l4.5 4.5 4.5-4.5" fill="none" stroke="#fff" stroke-width="2"/></svg></div>
      <div class="sec-body">
        <div class="row"><div class="chat"><svg width="18" height="14" viewBox="0 0 18 14"><ellipse cx="7" cy="6" rx="6.5" ry="4.8" fill="#555"/><path d="M3 9l-1.5 3.5 4-2z" fill="#555"/><ellipse cx="11.5" cy="8" rx="5" ry="3.8" fill="#555" stroke="#fff" stroke-width="1"/></svg></div><div class="info"><h3>Start Here!</h3><p>Nam vulputate justo vitae aliquam semper</p></div><div class="count"><b>6621</b><span>posts</span></div><div class="avatar"><svg width="14" height="14" viewBox="0 0 14 14"><circle cx="7" cy="4" r="3.3" fill="#333"/><path d="M1.5 14c0-4 2.5-5.5 5.5-5.5s5.5 1.5 5.5 5.5z" fill="#333"/></svg></div><div class="last"><strong>Thinking about joining the...</strong>By TrailLark<br>July 29</div></div>
        <div class="row"><div class="chat"><svg width="18" height="14" viewBox="0 0 18 14"><ellipse cx="7" cy="6" rx="6.5" ry="4.8" fill="#555"/><path d="M3 9l-1.5 3.5 4-2z" fill="#555"/><ellipse cx="11.5" cy="8" rx="5" ry="3.8" fill="#555" stroke="#fff" stroke-width="1"/></svg></div><div class="info"><h3>Ember Ridge Introductions</h3><p>Nam vulputate justo vitae aliquam semper senectus et netus et malesuada.</p></div><div class="count"><b>6621</b><span>posts</span></div><div class="avatar"><svg width="14" height="14" viewBox="0 0 14 14"><circle cx="7" cy="4" r="3.3" fill="#333"/><path d="M1.5 14c0-4 2.5-5.5 5.5-5.5s5.5 1.5 5.5 5.5z" fill="#333"/></svg></div><div class="last"><strong>Thinking about joining the...</strong>By TrailLark<br>July 29</div></div>
      </div>
    </section>

    <section class="section">
      <div class="sec-head">Ember Ridge Headquarters<svg width="12" height="8" viewBox="0 0 12 8"><path d="M1.5 1.5l4.5 4.5 4.5-4.5" fill="none" stroke="#fff" stroke-width="2"/></svg></div>
      <div class="sec-body">
        <div class="row"><div class="chat"><svg width="18" height="14" viewBox="0 0 18 14"><ellipse cx="7" cy="6" rx="6.5" ry="4.8" fill="#555"/><path d="M3 9l-1.5 3.5 4-2z" fill="#555"/><ellipse cx="11.5" cy="8" rx="5" ry="3.8" fill="#555" stroke="#fff" stroke-width="1"/></svg></div><div class="info"><h3>Nam vulputate justo</h3><p>Nam vulputate justo vitae aliquam semper</p></div><div class="count"><b>6621</b><span>posts</span></div><div class="avatar"><svg width="14" height="14" viewBox="0 0 14 14"><circle cx="7" cy="4" r="3.3" fill="#333"/><path d="M1.5 14c0-4 2.5-5.5 5.5-5.5s5.5 1.5 5.5 5.5z" fill="#333"/></svg></div><div class="last"><strong>Thinking about joining the...</strong>By TrailLark<br>July 29</div></div>
        <div class="row"><div class="chat"><svg width="18" height="14" viewBox="0 0 18 14"><ellipse cx="7" cy="6" rx="6.5" ry="4.8" fill="#555"/><path d="M3 9l-1.5 3.5 4-2z" fill="#555"/><ellipse cx="11.5" cy="8" rx="5" ry="3.8" fill="#555" stroke="#fff" stroke-width="1"/></svg></div><div class="info"><h3>The Woot Room</h3><p>Nam vulputate justo vitae aliquam semper senectus et netus et malesuada.</p></div><div class="count"><b>6621</b><span>posts</span></div><div class="avatar"><svg width="14" height="14" viewBox="0 0 14 14"><circle cx="7" cy="4" r="3.3" fill="#333"/><path d="M1.5 14c0-4 2.5-5.5 5.5-5.5s5.5 1.5 5.5 5.5z" fill="#333"/></svg></div><div class="last"><strong>Thinking about joining the...</strong>By TrailLark<br>July 29</div></div>
        <div class="row"><div class="chat"><svg width="18" height="14" viewBox="0 0 18 14"><ellipse cx="7" cy="6" rx="6.5" ry="4.8" fill="#555"/><path d="M3 9l-1.5 3.5 4-2z" fill="#555"/><ellipse cx="11.5" cy="8" rx="5" ry="3.8" fill="#555" stroke="#fff" stroke-width="1"/></svg></div><div class="info"><h3>Nam vulputate justo</h3><p>Nam vulputate justo vitae aliquam semper</p></div><div class="count"><b>6621</b><span>posts</span></div><div class="avatar"><svg width="14" height="14" viewBox="0 0 14 14"><circle cx="7" cy="4" r="3.3" fill="#333"/><path d="M1.5 14c0-4 2.5-5.5 5.5-5.5s5.5 1.5 5.5 5.5z" fill="#333"/></svg></div><div class="last"><strong>Thinking about joining the...</strong>By TrailLark<br>July 29</div></div>
        <div class="row"><div class="chat"><svg width="18" height="14" viewBox="0 0 18 14"><ellipse cx="7" cy="6" rx="6.5" ry="4.8" fill="#555"/><path d="M3 9l-1.5 3.5 4-2z" fill="#555"/><ellipse cx="11.5" cy="8" rx="5" ry="3.8" fill="#555" stroke="#fff" stroke-width="1"/></svg></div><div class="info"><h3>The Woot Room</h3><p>Nam vulputate justo vitae aliquam semper senectus et netus et malesuada.</p></div><div class="count"><b>6621</b><span>posts</span></div><div class="avatar"><svg width="14" height="14" viewBox="0 0 14 14"><circle cx="7" cy="4" r="3.3" fill="#333"/><path d="M1.5 14c0-4 2.5-5.5 5.5-5.5s5.5 1.5 5.5 5.5z" fill="#333"/></svg></div><div class="last"><strong>Thinking about joining the...</strong>By TrailLark<br>July 29</div></div>
      </div>
    </section>

    <section class="section">
      <div class="sec-head">General Fitness<svg width="12" height="8" viewBox="0 0 12 8"><path d="M1.5 1.5l4.5 4.5 4.5-4.5" fill="none" stroke="#fff" stroke-width="2"/></svg></div>
      <div class="sec-body">
        <div class="row"><div class="chat"><svg width="18" height="14" viewBox="0 0 18 14"><ellipse cx="7" cy="6" rx="6.5" ry="4.8" fill="#555"/><path d="M3 9l-1.5 3.5 4-2z" fill="#555"/><ellipse cx="11.5" cy="8" rx="5" ry="3.8" fill="#555" stroke="#fff" stroke-width="1"/></svg></div><div class="info"><h3>Nam vulputate justo</h3><p>Nam vulputate justo vitae aliquam semper</p></div><div class="count"><b>6621</b><span>posts</span></div><div class="avatar"><svg width="14" height="14" viewBox="0 0 14 14"><circle cx="7" cy="4" r="3.3" fill="#333"/><path d="M1.5 14c0-4 2.5-5.5 5.5-5.5s5.5 1.5 5.5 5.5z" fill="#333"/></svg></div><div class="last"><strong>Thinking about joining the...</strong>By TrailLark<br>July 29</div></div>
        <div class="row"><div class="chat"><svg width="18" height="14" viewBox="0 0 18 14"><ellipse cx="7" cy="6" rx="6.5" ry="4.8" fill="#555"/><path d="M3 9l-1.5 3.5 4-2z" fill="#555"/><ellipse cx="11.5" cy="8" rx="5" ry="3.8" fill="#555" stroke="#fff" stroke-width="1"/></svg></div><div class="info"><h3>The Woot Room</h3><p>Nam vulputate justo vitae aliquam semper senectus et netus et malesuada.</p></div><div class="count"><b>6621</b><span>posts</span></div><div class="avatar"><svg width="14" height="14" viewBox="0 0 14 14"><circle cx="7" cy="4" r="3.3" fill="#333"/><path d="M1.5 14c0-4 2.5-5.5 5.5-5.5s5.5 1.5 5.5 5.5z" fill="#333"/></svg></div><div class="last"><strong>Thinking about joining the...</strong>By TrailLark<br>July 29</div></div>
        <div class="row"><div class="chat"><svg width="18" height="14" viewBox="0 0 18 14"><ellipse cx="7" cy="6" rx="6.5" ry="4.8" fill="#555"/><path d="M3 9l-1.5 3.5 4-2z" fill="#555"/><ellipse cx="11.5" cy="8" rx="5" ry="3.8" fill="#555" stroke="#fff" stroke-width="1"/></svg></div><div class="info"><h3>Nam vulputate justo</h3><p>Nam vulputate justo vitae aliquam semper</p></div><div class="count"><b>6621</b><span>posts</span></div><div class="avatar"><svg width="14" height="14" viewBox="0 0 14 14"><circle cx="7" cy="4" r="3.3" fill="#333"/><path d="M1.5 14c0-4 2.5-5.5 5.5-5.5s5.5 1.5 5.5 5.5z" fill="#333"/></svg></div><div class="last"><strong>Thinking about joining the...</strong>By TrailLark<br>July 29</div></div>
        <div class="row"><div class="chat"><svg width="18" height="14" viewBox="0 0 18 14"><ellipse cx="7" cy="6" rx="6.5" ry="4.8" fill="#555"/><path d="M3 9l-1.5 3.5 4-2z" fill="#555"/><ellipse cx="11.5" cy="8" rx="5" ry="3.8" fill="#555" stroke="#fff" stroke-width="1"/></svg></div><div class="info"><h3>The Woot Room</h3><p>Nam vulputate justo vitae aliquam semper senectus et netus et malesuada.</p></div><div class="count"><b>6621</b><span>posts</span></div><div class="avatar"><svg width="14" height="14" viewBox="0 0 14 14"><circle cx="7" cy="4" r="3.3" fill="#333"/><path d="M1.5 14c0-4 2.5-5.5 5.5-5.5s5.5 1.5 5.5 5.5z" fill="#333"/></svg></div><div class="last"><strong>Thinking about joining the...</strong>By TrailLark<br>July 29</div></div>
      </div>
    </section>

    <section class="section">
      <div class="sec-head">Nutrition<svg width="12" height="8" viewBox="0 0 12 8"><path d="M1.5 1.5l4.5 4.5 4.5-4.5" fill="none" stroke="#fff" stroke-width="2"/></svg></div>
      <div class="sec-body">
        <div class="row"><div class="chat"><svg width="18" height="14" viewBox="0 0 18 14"><ellipse cx="7" cy="6" rx="6.5" ry="4.8" fill="#555"/><path d="M3 9l-1.5 3.5 4-2z" fill="#555"/><ellipse cx="11.5" cy="8" rx="5" ry="3.8" fill="#555" stroke="#fff" stroke-width="1"/></svg></div><div class="info"><h3>Start Here!</h3><p>Nam vulputate justo vitae aliquam semper</p></div><div class="count"><b>6621</b><span>posts</span></div><div class="avatar"><svg width="14" height="14" viewBox="0 0 14 14"><circle cx="7" cy="4" r="3.3" fill="#333"/><path d="M1.5 14c0-4 2.5-5.5 5.5-5.5s5.5 1.5 5.5 5.5z" fill="#333"/></svg></div><div class="last"><strong>Thinking about joining the...</strong>By TrailLark<br>July 29</div></div>
        <div class="row"><div class="chat"><svg width="18" height="14" viewBox="0 0 18 14"><ellipse cx="7" cy="6" rx="6.5" ry="4.8" fill="#555"/><path d="M3 9l-1.5 3.5 4-2z" fill="#555"/><ellipse cx="11.5" cy="8" rx="5" ry="3.8" fill="#555" stroke="#fff" stroke-width="1"/></svg></div><div class="info"><h3>Ember Ridge Introductions</h3><p>Nam vulputate justo vitae aliquam semper senectus et netus et malesuada.</p></div><div class="count"><b>6621</b><span>posts</span></div><div class="avatar"><svg width="14" height="14" viewBox="0 0 14 14"><circle cx="7" cy="4" r="3.3" fill="#333"/><path d="M1.5 14c0-4 2.5-5.5 5.5-5.5s5.5 1.5 5.5 5.5z" fill="#333"/></svg></div><div class="last"><strong>Thinking about joining the...</strong>By TrailLark<br>July 29</div></div>
      </div>
    </section>

    <section class="section">
      <div class="sec-head">Fitness Specialities<svg width="12" height="8" viewBox="0 0 12 8"><path d="M1.5 1.5l4.5 4.5 4.5-4.5" fill="none" stroke="#fff" stroke-width="2"/></svg></div>
      <div class="sec-body">
        <div class="row"><div class="chat"><svg width="18" height="14" viewBox="0 0 18 14"><ellipse cx="7" cy="6" rx="6.5" ry="4.8" fill="#555"/><path d="M3 9l-1.5 3.5 4-2z" fill="#555"/><ellipse cx="11.5" cy="8" rx="5" ry="3.8" fill="#555" stroke="#fff" stroke-width="1"/></svg></div><div class="info"><h3>Powerlifting and Weightlifting</h3><p>Nam vulputate justo vitae aliquam semper</p></div><div class="count"><b>6621</b><span>posts</span></div><div class="avatar"><svg width="14" height="14" viewBox="0 0 14 14"><circle cx="7" cy="4" r="3.3" fill="#333"/><path d="M1.5 14c0-4 2.5-5.5 5.5-5.5s5.5 1.5 5.5 5.5z" fill="#333"/></svg></div><div class="last"><strong>Thinking about joining the...</strong>By TrailLark<br>July 29</div></div>
        <div class="row"><div class="chat"><svg width="18" height="14" viewBox="0 0 18 14"><ellipse cx="7" cy="6" rx="6.5" ry="4.8" fill="#555"/><path d="M3 9l-1.5 3.5 4-2z" fill="#555"/><ellipse cx="11.5" cy="8" rx="5" ry="3.8" fill="#555" stroke="#fff" stroke-width="1"/></svg></div><div class="info"><h3>Bodyweight Strength Training</h3><p>Nam vulputate justo vitae aliquam semper senectus et netus et malesuada.</p></div><div class="count"><b>6621</b><span>posts</span></div><div class="avatar"><svg width="14" height="14" viewBox="0 0 14 14"><circle cx="7" cy="4" r="3.3" fill="#333"/><path d="M1.5 14c0-4 2.5-5.5 5.5-5.5s5.5 1.5 5.5 5.5z" fill="#333"/></svg></div><div class="last"><strong>Thinking about joining the...</strong>By TrailLark<br>July 29</div></div>
        <div class="row"><div class="chat"><svg width="18" height="14" viewBox="0 0 18 14"><ellipse cx="7" cy="6" rx="6.5" ry="4.8" fill="#555"/><path d="M3 9l-1.5 3.5 4-2z" fill="#555"/><ellipse cx="11.5" cy="8" rx="5" ry="3.8" fill="#555" stroke="#fff" stroke-width="1"/></svg></div><div class="info"><h3>Martial Arts</h3><p>Nam vulputate justo vitae aliquam semper</p></div><div class="count"><b>6621</b><span>posts</span></div><div class="avatar"><svg width="14" height="14" viewBox="0 0 14 14"><circle cx="7" cy="4" r="3.3" fill="#333"/><path d="M1.5 14c0-4 2.5-5.5 5.5-5.5s5.5 1.5 5.5 5.5z" fill="#333"/></svg></div><div class="last"><strong>Thinking about joining the...</strong>By TrailLark<br>July 29</div></div>
        <div class="row"><div class="chat"><svg width="18" height="14" viewBox="0 0 18 14"><ellipse cx="7" cy="6" rx="6.5" ry="4.8" fill="#555"/><path d="M3 9l-1.5 3.5 4-2z" fill="#555"/><ellipse cx="11.5" cy="8" rx="5" ry="3.8" fill="#555" stroke="#fff" stroke-width="1"/></svg></div><div class="info"><h3>Yoga, Meditation, Tai Chi</h3><p>Nam vulputate justo vitae aliquam semper senectus et netus et malesuada.</p></div><div class="count"><b>6621</b><span>posts</span></div><div class="avatar"><svg width="14" height="14" viewBox="0 0 14 14"><circle cx="7" cy="4" r="3.3" fill="#333"/><path d="M1.5 14c0-4 2.5-5.5 5.5-5.5s5.5 1.5 5.5 5.5z" fill="#333"/></svg></div><div class="last"><strong>Thinking about joining the...</strong>By TrailLark<br>July 29</div></div>
        <div class="row"><div class="chat"><svg width="18" height="14" viewBox="0 0 18 14"><ellipse cx="7" cy="6" rx="6.5" ry="4.8" fill="#555"/><path d="M3 9l-1.5 3.5 4-2z" fill="#555"/><ellipse cx="11.5" cy="8" rx="5" ry="3.8" fill="#555" stroke="#fff" stroke-width="1"/></svg></div><div class="info"><h3>Cross Training</h3><p>Nam vulputate justo vitae aliquam semper senectus et netus et malesuada.</p></div><div class="count"><b>6621</b><span>posts</span></div><div class="avatar"><svg width="14" height="14" viewBox="0 0 14 14"><circle cx="7" cy="4" r="3.3" fill="#333"/><path d="M1.5 14c0-4 2.5-5.5 5.5-5.5s5.5 1.5 5.5 5.5z" fill="#333"/></svg></div><div class="last"><strong>Thinking about joining the...</strong>By TrailLark<br>July 29</div></div>
        <div class="row"><div class="chat"><svg width="18" height="14" viewBox="0 0 18 14"><ellipse cx="7" cy="6" rx="6.5" ry="4.8" fill="#555"/><path d="M3 9l-1.5 3.5 4-2z" fill="#555"/><ellipse cx="11.5" cy="8" rx="5" ry="3.8" fill="#555" stroke="#fff" stroke-width="1"/></svg></div><div class="info"><h3>Running, Swimming, Biking, Walking, Hiking</h3><p>Nam vulputate justo vitae aliquam semper senectus et netus et malesuada.</p></div><div class="count"><b>6621</b><span>posts</span></div><div class="avatar"><svg width="14" height="14" viewBox="0 0 14 14"><circle cx="7" cy="4" r="3.3" fill="#333"/><path d="M1.5 14c0-4 2.5-5.5 5.5-5.5s5.5 1.5 5.5 5.5z" fill="#333"/></svg></div><div class="last"><strong>Thinking about joining the...</strong>By TrailLark<br>July 29</div></div>
      </div>
    </section>
    </div>

    <div class="sec-head collapsed" style="height:45px;margin-top:14px">Level Up Your Life<svg width="8" height="12" viewBox="0 0 8 12"><path d="M1.5 1.5l4.5 4.5-4.5 4.5" fill="none" stroke="#fff" stroke-width="2"/></svg></div>
    <div class="sec-head collapsed" style="height:45px">5 Week Challenges<svg width="8" height="12" viewBox="0 0 8 12"><path d="M1.5 1.5l4.5 4.5-4.5 4.5" fill="none" stroke="#fff" stroke-width="2"/></svg></div>
    <div class="sec-head collapsed" style="height:45px">Camp Ember Ridge<svg width="8" height="12" viewBox="0 0 8 12"><path d="M1.5 1.5l4.5 4.5-4.5 4.5" fill="none" stroke="#fff" stroke-width="2"/></svg></div>
  </main>

  <footer class="footer">
    <p>Copyright © 2019 Company Name .All Right Reserved. Privacy Policy / &nbsp;Contact Us</p>
    <div class="social" aria-label="Social links"><i></i><i></i><i></i><i></i><i></i></div>
  </footer>
</div>
</body>
</html>
```